Brochure for new townhouse development

We need a brochure created for our new townhouse development that we can provide to potential purchasers for off-the-plan sales.

2 similar examples are attached.

Brochure content is to include the text as per the attached word document (brochure text) and as follows:
Cover
The Development
At a Glance
The Location - also to include the 2d map and aerial photo (have included screenshot of map and aerial photo as a placeholder, to be replaced in the final version)
Plans - include 3d floor plans, I have included a sample 3d floor plan as a placeholder, this is to be replaced in the final version.
Finishes - as per word document attached, and colour samples attached
Specifications - as per word document attached
Subdivision plan - I have attached a plan which can be used as a placeholder, the final version will be ready next week and is to be replaced in the final version
Landscape plan - as per attached
Rental assessment - as per attached
Stake your Claim

Renders of the building are attached and can be used throughout the brochure.

There is no company name or logo to include.

We have other upcoming developments and would look to reuse the winning brochure so there is future and ongoing work.

```html
<!DOCTYPE html>
<html lang="en">
<head>
<meta charset="utf-8">
<title>The Development</title>
<link rel="stylesheet" href="https://fonts.googleapis.com/css2?family=Montserrat:wght@400;500;700&display=swap">
<style>
  :root {
    --page: #ffffff;
    --ink: #2b2424;
    --body-ink: #2e2a2a;
    --accent: #0aa0e6;
    --rule: #ececec;
    --tone-top: #c6e6fb;
    --tone-mid: #d9d2cf;
    --tone-low: #8c8f90;
  }
  * { box-sizing: border-box; margin: 0; padding: 0; }
  html, body {
    width: 1200px;
    height: 849px;
    overflow: hidden;
    background: var(--page);
  }
  .spread {
    position: relative;
    width: 1200px;
    height: 849px;
    background: var(--page);
    font-family: "Montserrat", sans-serif;
  }
  .content-frame {
    position: absolute;
    left: 0;
    top: 81px;
    width: 1121px;
    height: 688px;
    border: 1px solid var(--rule);
    border-left: none;
  }
  .hero-render {
    position: absolute;
    left: 0;
    top: 81px;
    width: 626px;
    height: 688px;
    background: linear-gradient(180deg, var(--tone-top) 0%, var(--tone-mid) 55%, var(--tone-low) 100%);
  }
  .section-title {
    position: absolute;
    left: 581px;
    top: 149px;
    width: 326px;
    height: 48px;
    border: 2px solid var(--accent);
    display: flex;
    align-items: center;
  }
  .section-title .corner {
    position: absolute;
    left: 0;
    top: 0;
    width: 44px;
    height: 44px;
  }
  .section-title h1 {
    margin-left: 80px;
    font-size: 23px;
    font-weight: 700;
    color: var(--ink);
    letter-spacing: 0.1px;
  }
  .copy {
    position: absolute;
    left: 663px;
    top: 249px;
    width: 425px;
    color: var(--body-ink);
    font-size: 12.9px;
    font-weight: 400;
    line-height: 17.8px;
    text-align: justify;
    letter-spacing: -0.2px;
  }
  .copy p + p { margin-top: 13.6px; }
</style>
</head>
<body>
  <main class="spread">
    <div class="content-frame"></div>
    <div class="hero-render" role="img" aria-label="Architectural render of the two-storey townhouses with driveway"></div>

    <header class="section-title">
      <svg class="corner" viewBox="0 0 44 44" aria-hidden="true">
        <polygon points="44,0 44,44 0,44" fill="var(--accent)"/>
      </svg>
      <h1>The Development</h1>
    </header>

    <section class="copy">
      <p>24 Larchmont Road, Ashbury, is a brand-new development of six contemporary townhouses in an unrivalled location, poised to enjoy a vibrant urban lifestyle within easy reach of Ashbury Village and the city, and zoned for top schools.</p>
      <p>Two blocks of three residences offer stylish, hassle-free living. Each townhouse comprises two bedrooms, two en suite bathrooms, single internal-access garage and private courtyard. Smart design, premium finishes and freehold titles ensure a quality project with a premium address.</p>
      <p>On the ground floor, open-plan living and dining flows to a low-maintenance courtyard garden for outdoor living and entertaining. Connected by a breakfast bar, a sleek, chic and functional kitchen boasts high-quality appliances.</p>
      <p>Upstairs are two double bedrooms, each served by a high-spec tiled en suite bathroom. Two of the townhouses feature a walk-in robe in the master, while other bedrooms include built-in wardrobes.</p>
      <p>A downstairs guest WC and single internal-access garage with laundry add superb convenience.</p>
      <p>Architecturally designed by Halden Architecture, these homes are scheduled for completion by the end of 2021. Developments of this quality – in a location of this calibre – are all too rare, so this is the time to make your move.</p>
    </section>
  </main>
</body>
</html>
```